Stationary Design for Energy Trading & Supply Company
Business Cards, Stationary, PowerPoint template, word template for letters and documentations
Creative Brief
Professional
Martin Keslowe
Executive Director
Suite 18B, Floor 41, Corvana Business Tower (Corvana Tower North) Halden Parkway Road, Market Quarter 5 Dubai, United Arab Emirates
m@q.example
www.tribeca-volt.example
email is martin.keslowe@tribeca-volt.example
just the icon with website below www.tribeca-volt.example

```html
<!DOCTYPE html>
<html lang="en">
<head>
<meta charset="utf-8">
<title>Tribeca Volt – Stationery</title>
<link href="https://fonts.googleapis.com/css2?family=Montserrat:wght@400;500;600;700;800&family=Open+Sans:wght@400;600&display=swap" rel="stylesheet">
<style>
  :root{
    --navy:#1c2a4a;
    --navy-deep:#14203b;
    --blue:#2b7fc2;
    --sky:#4fa3dc;
    --ink:#2d3340;
    --muted:#6c7380;
    --paper:#ffffff;
    --stage:#e9e6e1;
    --watermark:#eef0f3;
  }
  *{box-sizing:border-box;margin:0;padding:0}
  html,body{width:1200px;height:1070px;overflow:hidden;background:var(--stage)}
  body{position:relative;font-family:"Open Sans",Arial,sans-serif;color:var(--ink)}

  .card,.letterhead{position:absolute;background:var(--paper);overflow:hidden;box-shadow:0 6px 18px rgba(0,0,0,.18)}
  .card{border-radius:16px}

  .brand{display:flex;align-items:center;gap:14px}
  .brand-dot{border-radius:50%;background:var(--blue);flex:none}
  .brand-name{font-family:"Montserrat",Arial,sans-serif;font-weight:800;color:var(--navy);line-height:.95;letter-spacing:.02em}
  .tagline{font-family:"Montserrat",Arial,sans-serif;font-weight:600;color:var(--navy);letter-spacing:.06em;text-transform:uppercase;white-space:nowrap}

  .card-front{left:80px;top:280px;width:465px;height:372px}
  .card-front .lockup{position:absolute;left:0;right:0;top:105px;display:flex;flex-direction:column;align-items:center;gap:14px}
  .card-front .brand{flex-direction:column;gap:12px}
  .card-front .brand-dot{width:70px;height:70px}
  .card-front .brand-name{font-size:44px}
  .card-front .tagline{font-size:11.5px}
  .card-front .band{position:absolute;left:0;bottom:0;width:100%;height:60px}

  .card-back{left:80px;top:696px;width:465px;height:312px}
  .card-back .brand{position:absolute;left:24px;top:70px;flex-direction:column;align-items:flex-start;gap:8px}
  .card-back .brand-row{display:flex;align-items:center;gap:10px}
  .card-back .brand-dot{width:36px;height:36px}
  .card-back .brand-name{font-size:25px}
  .card-back .tagline{font-size:6.3px}
  .card-back .divider{position:absolute;left:208px;top:60px;width:1px;height:150px;background:#c9ced6}
  .contact{position:absolute;left:222px;top:56px;width:230px}
  .contact .person{font-family:"Montserrat",Arial,sans-serif;font-weight:700;font-size:19px;color:var(--navy)}
  .contact .role{font-size:10.5px;color:var(--ink);margin-top:2px}
  .contact .address{font-size:8.6px;line-height:1.45;margin-top:9px}
  .contact ul{list-style:none;margin-top:8px}
  .contact li{display:flex;align-items:center;gap:6px;font-size:8.6px;line-height:1.7}
  .icon{width:10px;height:10px;flex:none}
  .card-back .band{position:absolute;left:0;bottom:0;width:100%;height:56px}

  .letterhead{left:560px;top:143px;width:557px;height:860px}
  .letterhead .brand{position:absolute;left:44px;top:48px;flex-direction:column;align-items:flex-start;gap:6px}
  .letterhead .brand-row{display:flex;align-items:center;gap:9px}
  .letterhead .brand-dot{width:30px;height:30px}
  .letterhead .brand-name{font-size:21px}
  .letterhead .tagline{font-size:5.5px}
  .lh-contact{position:absolute;left:345px;top:40px;width:190px;padding-left:10px;border-left:1px solid #c9ced6}
  .lh-contact .address{font-size:6.8px;line-height:1.4}
  .lh-contact ul{list-style:none;margin-top:5px}
  .lh-contact li{display:flex;align-items:center;gap:5px;font-size:6.8px;line-height:1.7}
  .lh-contact .icon{width:8px;height:8px}
  .watermark{position:absolute;left:170px;top:250px;width:220px;height:220px;border-radius:50%;background:var(--watermark)}
  .letter{position:absolute;left:44px;top:165px;width:470px;font-size:7.4px;line-height:1.7;color:#4a505b}
  .recipient .name{font-weight:600;color:var(--ink);text-transform:uppercase;letter-spacing:.03em}
  .letter p{margin-top:14px;text-align:justify}
  .signoff{margin-top:30px}
  .signature{font-family:"Montserrat",Arial,sans-serif;font-weight:600;font-size:11px;color:var(--navy);margin:8px 0 2px}
  .letterhead .band{position:absolute;left:0;bottom:0;width:100%;height:38px}
</style>
</head>
<body>

<section class="card card-front">
  <div class="lockup">
    <div class="brand">
      <span class="brand-dot"></span>
      <span class="brand-name">TRIBECA VOLT</span>
    </div>
    <div class="tagline">Clarity in Markets – Strength in Delivery</div>
  </div>
  <svg class="band" viewBox="0 0 465 60" preserveAspectRatio="none">
    <path d="M0 28 Q232 4 465 28 L465 60 L0 60 Z" fill="var(--blue)"/>
    <path d="M0 36 Q232 14 465 36 L465 60 L0 60 Z" fill="var(--navy)"/>
  </svg>
</section>

<section class="card card-back">
  <div class="brand">
    <div class="brand-row">
      <span class="brand-dot"></span>
      <span class="brand-name">TRIBECA<br>VOLT</span>
    </div>
    <div class="tagline">Clarity in Markets – Strength in Delivery</div>
  </div>
  <div class="divider"></div>
  <div class="contact">
    <div class="person">Martin Keslowe</div>
    <div class="role">Executive Director</div>
    <div class="address">Suite 18B, Floor 41,<br>Corvana Business Tower (Corvana Tower North)<br>Halden Parkway Road, Market Quarter 5<br>Dubai, United Arab Emirates</div>
    <ul>
      <li><svg class="icon" viewBox="0 0 10 10"><circle cx="5" cy="5" r="5" fill="var(--blue)"/><path d="M3 2.5l1 1-.5.8c.4.8 1 1.4 1.8 1.8l.8-.5 1 1-.7.9C4.8 7.3 2.7 5.2 2.5 3.2z" fill="#fff"/></svg>+971 555 013 274</li>
      <li><svg class="icon" viewBox="0 0 10 10"><circle cx="5" cy="5" r="5" fill="var(--blue)"/><rect x="2.4" y="3.2" width="5.2" height="3.6" fill="none" stroke="#fff" stroke-width=".7"/><path d="M2.4 3.2L5 5.3l2.6-2.1" fill="none" stroke="#fff" stroke-width=".7"/></svg>martin.keslowe@tribeca-volt.example</li>
      <li><svg class="icon" viewBox="0 0 10 10"><circle cx="5" cy="5" r="5" fill="var(--blue)"/><circle cx="5" cy="5" r="2.6" fill="none" stroke="#fff" stroke-width=".7"/><path d="M2.4 5h5.2M5 2.4v5.2" stroke="#fff" stroke-width=".6"/></svg>www.tribeca-volt.example</li>
    </ul>
  </div>
  <svg class="band" viewBox="0 0 465 56" preserveAspectRatio="none">
    <path d="M0 30 L280 30 Q330 30 360 18 L465 18 L465 56 L0 56 Z" fill="var(--blue)"/>
    <path d="M0 36 L290 36 Q340 36 370 26 L465 26 L465 56 L0 56 Z" fill="var(--navy)"/>
  </svg>
</section>

<section class="letterhead">
  <div class="brand">
    <div class="brand-row">
      <span class="brand-dot"></span>
      <span class="brand-name">TRIBECA<br>VOLT</span>
    </div>
    <div class="tagline">Clarity in Markets – Strength in Delivery</div>
  </div>
  <div class="lh-contact">
    <div class="address">Suite 18B, Floor 41,<br>Corvana Business Tower (Corvana Tower North)<br>Halden Parkway Road, Market Quarter 5<br>Dubai, United Arab Emirates</div>
    <ul>
      <li><svg class="icon" viewBox="0 0 10 10"><circle cx="5" cy="5" r="5" fill="var(--blue)"/></svg>+971 555 013 274</li>
      <li><svg class="icon" viewBox="0 0 10 10"><circle cx="5" cy="5" r="5" fill="var(--blue)"/></svg>martin.keslowe@tribeca-volt.example</li>
      <li><svg class="icon" viewBox="0 0 10 10"><circle cx="5" cy="5" r="5" fill="var(--blue)"/></svg>www.tribeca-volt.example</li>
    </ul>
  </div>

  <div class="watermark" role="img" aria-label="Faint brand mark decoration"></div>

  <div class="letter">
    <div class="recipient">
      <div class="name">Noelle Varga</div>
      <div>Chief Business Officer</div>
      <div>City Name, City Code</div>
    </div>
    <p>Thank you for your continued partnership with our trading desk. This letter confirms the supply schedule agreed during our recent review, including delivery windows, pricing terms and quality standards for the coming quarter. Our team will share updated volume forecasts each month and remain available to support any changes your operations may require.</p>
    <p>We are committed to transparent reporting and reliable logistics across every shipment. Please review the attached summary and confirm the contact details for your receiving terminal so that documentation can be finalised without delay.</p>
    <p>Should you have any questions, our commercial team will be pleased to assist you.</p>
    <div class="signoff">
      <div>Regards,</div>
      <div class="signature">Priya Danvers</div>
      <div>Priya Danvers</div>
    </div>
  </div>

  <svg class="band" viewBox="0 0 557 38" preserveAspectRatio="none">
    <path d="M0 16 L330 16 Q380 16 410 6 L557 6 L557 38 L0 38 Z" fill="var(--blue)"/>
    <path d="M0 22 L340 22 Q390 22 420 13 L557 13 L557 38 L0 38 Z" fill="var(--navy)"/>
  </svg>
</section>

</body>
</html>
```